Spiral Bound Classy Marketing Planner Cover Design

A5 marketing planner book cover requiredClassy, minimalist design for female entrepreneurs. The inside is all in grey and is a minimalist uncluttered design. Name of the planner is It's Time Marketing Recipe PlannerHeader font inside the planner is Shelby and other font is Lato Brand colours are teal and grey.The printing format has changed and as such I am looking for a new cover design to make this marketing planner look classy and engaging. Would prefer my logo to be on the back. We have the option for a 10cm x 10cm foil detail to be added on the front cover, feel free to add this to your design.This is for a spiral bound book - A5 front cover and A5 back cover - no spine required.

Target Market(s)

Female entrepreneurs

Industry/Entity Type

Marketing

Colors
33b8a4
ffffff

Requirements
Must have
• Front and back designs
• A5
Should not have
• Large illustrations
• People in the design
• Spine design

```html
<!DOCTYPE html>
<html lang="en">
<head>
<meta charset="utf-8">
<title>Bright Path Promotion Blueprint Planner — Front Cover</title>
<link rel="stylesheet" href="https://fonts.googleapis.com/css2?family=Dancing+Script:wght@500&family=Lato:wght@300&display=swap">
<style>
  :root {
    --backdrop: #5fffa4;
    --accent: #5cf0a6;
    --panel: #f4f7f6;
    --ink-dark: #2b2f30;
    --ink-mid: #6b7172;
    --ink-light: #e6e8e8;
  }
  * { box-sizing: border-box; margin: 0; padding: 0; }
  html, body {
    width: 1200px;
    height: 1200px;
    overflow: hidden;
    background: var(--backdrop);
  }
  .canvas {
    position: relative;
    width: 1200px;
    height: 1200px;
    background: var(--backdrop);
  }
  .cover {
    position: absolute;
    left: 211px;
    top: 50px;
    width: 778px;
    height: 1100px;
    overflow: hidden;
  }
  .cover-art {
    position: absolute;
    inset: 0;
    background:
      radial-gradient(ellipse 45% 30% at 30% 40%, rgba(230,232,232,0.85), transparent 70%),
      radial-gradient(ellipse 55% 30% at 45% 85%, rgba(240,242,242,0.95), transparent 75%),
      radial-gradient(ellipse 40% 25% at 80% 30%, rgba(200,204,205,0.7), transparent 70%),
      linear-gradient(165deg, var(--ink-dark) 0%, #3d4243 35%, var(--ink-mid) 60%, var(--ink-light) 85%);
  }
  .title-frame {
    position: absolute;
    left: 205px;
    top: 285px;
    width: 420px;
    height: 440px;
    border: 10px solid var(--accent);
  }
  .title-panel {
    position: absolute;
    left: 240px;
    top: 305px;
    width: 400px;
    height: 400px;
    background: var(--panel);
    display: flex;
    flex-direction: column;
    align-items: center;
    padding-top: 50px;
    color: var(--accent);
    text-align: center;
  }
  .title-script {
    font-family: "Dancing Script", cursive;
    font-weight: 500;
    font-size: 78px;
    line-height: 1;
  }
  .title-rule {
    width: 300px;
    height: 2px;
    background: var(--accent);
    margin: 28px 0 26px;
  }
  .title-sub {
    font-family: "Lato", sans-serif;
    font-weight: 300;
    font-size: 40px;
    line-height: 1.08;
    letter-spacing: 2px;
    text-transform: uppercase;
  }
</style>
</head>
<body>
  <main class="canvas">
    <section class="cover">
      <div class="cover-art" role="img" aria-label="Abstract black, grey and white fluid marble texture"></div>
      <div class="title-frame"></div>
      <div class="title-panel">
        <h1 class="title-script">Bright Path</h1>
        <div class="title-rule"></div>
        <p class="title-sub">Promotion<br>Blueprint<br>Planner</p>
      </div>
    </section>
  </main>
</body>
</html>
```